the theater production needs a poster design

we need a poster design for a theater drama in Seoul , South Korea.

the title : THE LANTERN KEEPER'S ROAD
BASED ON WALTER DREVICK'S BOOK

where:Haneulbit Stagehouse, Jongro-Gu, Seoul
when:2022.1.1~OpenRun
Saturday 3PM, 63PM, Sunday 5pm, Monday 7:30pm

TICKET PRICE: $45

BOOK NOW
02 471 6039
RIVA TROUPE

Director Minha Park Composer Sora Lee, Sound Director Doyun Han
Producer Taesik Yoon

Target Market(s)

for Chiristan and others

Industry/Entity Type

Christian community and non Christian society

Colors
0094D4
00A9DD
6FCCEA
C7EBF8
E9F6FB

Requirements
Must have
• the main Character, pilgrim should should carry some burdens on his shoulder

```html
<!DOCTYPE html>
<html lang="en">
<head>
<meta charset="utf-8">
<title>The Lantern Keeper's Road – Poster</title>
<link href="https://fonts.googleapis.com/css2?family=Poppins:ital,wght@0,300;0,500;0,700;0,800;1,900&display=swap" rel="stylesheet">
<style>
  :root {
    --page: #ffffff;
    --sky-top: #9fb8b4;
    --sky-glow: #f1ead2;
    --rock: #3a2b3a;
    --sand: #6e4a4c;
    --sand-deep: #2a1a22;
    --ink: #1f2530;
    --ink-top: #4a5260;
    --gold: #e8b948;
    --gold-light: #f6d98a;
    --white: #ffffff;
    --silver: #d9dadd;
  }
  * { box-sizing: border-box; margin: 0; padding: 0; }
  html, body { width: 1188px; height: 1200px; overflow: hidden; background: var(--page); }
  body { position: relative; font-family: "Poppins", sans-serif; }

  .poster {
    position: absolute; left: 208px; top: 59px; width: 768px; height: 1077px;
    overflow: hidden; color: var(--white);
  }
  .poster__scene {
    position: absolute; inset: 0;
    background:
      radial-gradient(ellipse 70% 22% at 65% 38%, rgba(241,234,210,.85), rgba(241,234,210,0) 70%),
      linear-gradient(180deg, var(--sky-top) 0%, var(--sky-glow) 30%, #c9a995 40%, var(--rock) 48%, var(--sand) 62%, #4a2f36 80%, var(--sand-deep) 100%);
  }
  .poster__scene-fade {
    position: absolute; left: 0; right: 0; bottom: 0; height: 300px;
    background: linear-gradient(180deg, rgba(20,12,18,0), rgba(20,12,18,.85));
  }

  .pill {
    position: absolute;
    background: linear-gradient(180deg, var(--ink-top), var(--ink) 60%);
    border: 2px solid rgba(255,255,255,.85);
    box-shadow: 0 4px 10px rgba(0,0,0,.45);
    display: flex; align-items: center; justify-content: center; text-align: center;
  }
  .pill--label { border-radius: 30px; z-index: 2; }
  .pill--value { border-radius: 0 0 22px 22px; border-top: none; }
  .gold-text {
    font-weight: 800; letter-spacing: .5px;
    background: linear-gradient(180deg, var(--gold-light), var(--gold) 60%, #c7922e);
    -webkit-background-clip: text; background-clip: text; color: transparent;
  }

  .booking__label { left: 454px; top: 40px; width: 283px; height: 69px; font-size: 33px; }
  .booking__contact { left: 486px; top: 107px; width: 220px; height: 81px; flex-direction: column;
    font-size: 22px; font-weight: 500; line-height: 1.15; }

  .title { position: absolute; left: 0; right: 0; top: 600px; text-align: center; }
  .title__lead { font-size: 44px; font-weight: 800; letter-spacing: -1px; line-height: 1;
    background: linear-gradient(180deg, #fff, var(--silver)); -webkit-background-clip: text; background-clip: text; color: transparent;
    filter: drop-shadow(0 3px 3px rgba(0,0,0,.5)); }
  .title__main { margin-top: 6px; font-size: 112px; font-weight: 900; font-style: italic; letter-spacing: -3px; line-height: 1;
    background: linear-gradient(180deg, #fff 30%, #c9cbd0); -webkit-background-clip: text; background-clip: text; color: transparent;
    filter: drop-shadow(0 4px 4px rgba(0,0,0,.55)); }
  .title__flare { position: absolute; left: 40px; right: 0; height: 2px;
    background: linear-gradient(90deg, rgba(232,185,72,0), rgba(246,217,138,.9) 50%, rgba(232,185,72,0)); }
  .title__source { position: absolute; left: 0; right: 0; top: 772px; text-align: center;
    font-size: 24px; font-weight: 500; letter-spacing: -.3px; text-shadow: 0 2px 3px rgba(0,0,0,.6); }

  .ticket__label { left: 43px; top: 850px; width: 222px; height: 55px; font-size: 26px; }
  .ticket__price { left: 91px; top: 903px; width: 127px; height: 60px; font-size: 36px; font-weight: 800; }

  .schedule { position: absolute; left: 284px; top: 842px; height: 133px; border-left: 3px solid var(--white); padding-left: 17px; width: 460px; }
  .schedule__venue { font-size: 16px; font-weight: 800; letter-spacing: .2px; margin-top: 2px; }
  .schedule__dates { font-size: 39px; line-height: 1.1; margin-top: -1px; }
  .schedule__rule { height: 3px; background: var(--white); width: 420px; margin: 5px 0 8px; }
  .schedule__times { font-size: 19.5px; font-weight: 800; line-height: 1.3; letter-spacing: -.2px; }

  .credits { position: absolute; left: 0; right: 0; top: 1014px; text-align: center;
    font-size: 17px; font-weight: 300; line-height: 1.3; }
</style>
</head>
<body>
  <main class="poster">
    <div class="poster__scene" role="img" aria-label="Desert landscape at dawn with mountains, a line of robed pilgrims walking along a sandy path, the lead pilgrim carrying a heavy burden on his shoulders"></div>
    <div class="poster__scene-fade"></div>

    <div class="pill pill--label booking__label"><span class="gold-text">BOOK NOW</span></div>
    <div class="pill pill--value booking__contact"><span>02 471 6039</span><span>RIVA TROUPE</span></div>

    <header class="title">
      <div class="title__flare" style="top:24px"></div>
      <div class="title__flare" style="top:160px"></div>
      <div class="title__lead">THE LANTERN KEEPER'S</div>
      <div class="title__main">ROAD</div>
    </header>
    <p class="title__source">BASED ON WALTER DREVICK'S BOOK</p>

    <div class="pill pill--label ticket__label"><span class="gold-text">TICKET PRICE</span></div>
    <div class="pill pill--value ticket__price">$45</div>

    <section class="schedule">
      <p class="schedule__venue">HANEULBIT STAGEHOUSE, JONGRO-GU, SEOUL</p>
      <p class="schedule__dates gold-text">2022.1.1~OPENRUN</p>
      <div class="schedule__rule"></div>
      <p class="schedule__times">SATURDAY 3PM, 63PM, SUNDAY 5PM,<br>MONDAY 7:30PM</p>
    </section>

    <footer class="credits">
      Director Minha Park, Composer Sora Lee,<br>
      Sound Director Doyun Han, Producer Taesik Yoon
    </footer>
  </main>
</body>
</html>
```